Inspiration Poster

Inspirational Poster that has a Kamran Dulo like abstract look (http://www.vexalo.com/images/search?q=kamran+dulo&FORM=HDRSC2) with the text:

"we walk not in order to arrive at the promise land but because walking itself is a revolution"
-Peter Ambrick

```html
<!DOCTYPE html>
<html lang="en">
<head>
<meta charset="utf-8">
<title>Inspiration Poster</title>
<link rel="stylesheet" href="https://fonts.googleapis.com/css2?family=Advent+Pro:wght@500;600&display=swap">
<style>
  :root {
    --sky-top: #8ccbea;
    --sky-mid: #d3ecf8;
    --paper: #ffffff;
    --ink: #1c1c1c;
    --curve-line: #8cc45a;
    --ground-top: #e2e3ec;
    --ground-bottom: #a6a8c8;
  }
  html, body {
    margin: 0;
    padding: 0;
    overflow: hidden;
    background: var(--paper);
  }
  .poster {
    position: relative;
    width: 854px;
    height: 1200px;
    overflow: hidden;
    background: linear-gradient(to bottom, var(--sky-top) 0%, var(--sky-mid) 45%, var(--paper) 68%);
    font-family: "Advent Pro", "Arial Narrow", sans-serif;
    color: var(--ink);
  }
  .quote {
    position: absolute;
    top: 398px;
    left: 20px;
    width: 802px;
    margin: 0;
    font-weight: 500;
    font-size: 41px;
    line-height: 64px;
    letter-spacing: 0.4px;
  }
  .quote-line {
    display: block;
    white-space: nowrap;
  }
  .quote-line--second {
    text-align: right;
  }
  .author {
    position: absolute;
    top: 562px;
    right: 34px;
    margin: 0;
    font-weight: 600;
    font-size: 54px;
    line-height: 64px;
  }
  .ground {
    position: absolute;
    left: 0;
    bottom: 0;
    width: 854px;
    height: 430px;
    display: block;
  }
</style>
</head>
<body>
<main class="poster">
  <blockquote class="quote">
    <span class="quote-line">"we walk not in order to arrive at the promise land</span>
    <span class="quote-line quote-line--second">but because walking itself is a revolution"</span>
  </blockquote>
  <p class="author">-Peter Ambrick</p>

  <svg class="ground" viewBox="0 0 854 430" xmlns="http://www.w3.org/2000/svg">
    <defs>
      <linearGradient id="ground-fill" x1="0" y1="0" x2="0" y2="1">
        <stop offset="0" stop-color="var(--ground-top)"/>
        <stop offset="1" stop-color="var(--ground-bottom)"/>
      </linearGradient>
    </defs>
    <path class="ground-area" role="img" aria-label="Abstract band of soft grey and lavender vertical tones"
          d="M0 132 C 250 132 560 114 854 44 L854 430 L0 430 Z" fill="url(#ground-fill)"/>
    <path class="horizon-curve" d="M0 131 C 250 131 560 113 854 43"
          fill="none" stroke="var(--curve-line)" stroke-width="8"/>
  </svg>
</main>
</body>
</html>
```